Hardware Brand Packaging Design Project

We require a design for packaging for products in the retail hardware range. Initially this will be for a set of header cards for abrasive sanding discs but we plan to add other items to the range so we are looking for a range of brand elements that can be extended to other types of packaging.
The brand name is "Lumen Ridge" and we are looking for a black or dark grey background with a subtle fine pattern to break up the solid colour. This part of the design needs to be 'expandable' so that it can be used on different pack sizes as we increase the range. Two highlight or complimentary colours will add a bit of impact and become part of the brand style.
For printing purposes we have allowed for 4 colour process plus two spot colours and we have attached one of the header card dielines as a guide.
Target Market(s)
Home owners of both gender in the 25 to 55 age range
Industry/Entity Type
Printing
Requirements
Must have
- *The brand name "Lumen Ridge" should appear in the top left hand corner and we had in mind that the word would be a shiny metal / chrome appearance in could be in the shape of a shield or spear point but are open to any other suggestions.The word can be on one line or one above the other.
*Between the bottom of the hanger hole and the edge of the card is the words ABRASIVES & ACCESSORIES
*We want a performance guarantee device circle / seal or other in the bottom left quartile of the front facing panel. Circle device on attachment shows approx position.
* The right hand 25mm of the card is to be devoted to specific information about the product in the pack. This will be done by an adhered over-sticker ( see attached die-line No 2 )
* 3 line address panel or rear of card - QRV Abrasives, 456 Lane, West Auckland, New Zealand.
* Also somewhere on rear panel "Cut, Quality Checked & Packed in New Zealand from imported materials."
Nice to have
- It would be good, but not essential, to see a rough mock-up of how this design would transfer across to a box approx 80mm across the front, 100mm deep and 250mm high.

```html
<!DOCTYPE html>
<html lang="en">
<head>
<meta charset="utf-8">
<title>Lumen Ridge – Sanding Disc Header Card</title>
<link href="https://fonts.googleapis.com/css2?family=Libre+Baskerville:wght@400;700&display=swap" rel="stylesheet">
<style>
  :root {
    --paper: #ffffff;
    --card-black: #121212;
    --card-dark: #1e1e22;
    --cream: #fbf6b6;
    --steel: #a9bcc4;
    --grey: #8a8a8a;
    --plum: #2e2850;
    --ink: #000000;
    --dim-pink: #d64fd8;
    --dim-blue: #4a90e8;
    --fold-green: #8fcf6a;
    --fold-pink: #e48ab0;
  }
  html, body {
    margin: 0;
    padding: 0;
    width: 1139px;
    height: 1200px;
    overflow: hidden;
    background: var(--paper);
  }
  .artboard {
    position: relative;
    width: 1139px;
    height: 1200px;
    font-family: "Libre Baskerville", "Times New Roman", serif;
  }
  .artboard svg { position: absolute; left: 0; top: 0; }
  .dim-label {
    font-family: Arial, Helvetica, sans-serif;
    font-size: 40px;
    fill: var(--ink);
  }
  .serif { font-family: "Libre Baskerville", "Times New Roman", serif; }
  .bold { font-weight: 700; }
</style>
</head>
<body>
<div class="artboard">
  <svg width="1139" height="1200" viewBox="0 0 1139 1200" xmlns="http://www.w3.org/2000/svg">
    <defs>
      <clipPath id="card-shape">
        <path d="M262 18 H370 Q690 170 1015 18 H1091 Q1104 18 1104 31 V787 Q1104 800 1091 800 H1010 Q680 600 340 800 H262 Q249 800 249 787 V31 Q249 18 262 18 Z"/>
      </clipPath>
      <linearGradient id="card-fill" x1="0" y1="0" x2="1" y2="1">
        <stop offset="0" stop-color="var(--card-dark)"/>
        <stop offset="1" stop-color="var(--card-black)"/>
      </linearGradient>
    </defs>

    <!-- height dimension -->
    <g class="dimension dimension-height" stroke="var(--dim-pink)" stroke-width="2">
      <line x1="110" y1="28" x2="110" y2="810"/>
      <line x1="90" y1="28" x2="250" y2="28"/>
      <line x1="90" y1="810" x2="250" y2="810"/>
    </g>
    <text class="dim-label" x="46" y="425" text-anchor="middle" transform="rotate(-90 46 425)" dy="14">120</text>

    <!-- width dimension -->
    <g class="dimension dimension-width" stroke="var(--dim-blue)" stroke-width="2">
      <line x1="249" y1="913" x2="1104" y2="913"/>
      <line x1="249" y1="820" x2="249" y2="935"/>
      <line x1="1104" y1="820" x2="1104" y2="935"/>
    </g>
    <text class="dim-label" x="684" y="965" text-anchor="middle">130</text>

    <!-- header card -->
    <g class="header-card" clip-path="url(#card-shape)">
      <rect class="card-field" x="249" y="18" width="855" height="782" fill="url(#card-fill)" role="img" aria-label="Dark card background with a subtle fine pattern"/>
      <rect class="info-panel" x="886" y="18" width="218" height="782" fill="var(--cream)"/>

      <line class="fold-line" x1="249" y1="184" x2="1104" y2="184" stroke="var(--fold-green)" stroke-width="2" stroke-dasharray="6 5"/>
      <line class="fold-line" x1="249" y1="405" x2="1104" y2="405" stroke="var(--fold-pink)" stroke-width="2" stroke-dasharray="6 5"/>
    </g>

    <!-- hanger hole die-cut -->
    <path class="hanger-hole" fill="var(--paper)"
      d="M440 403 L525 282 Q530 275 540 275 H760 Q772 275 772 287 V335 Q772 347 760 347 H740
         A22 22 0 0 1 700 347 A22 22 0 0 0 660 347 A22 22 0 0 1 620 347 A22 22 0 0 0 580 347 H560
         Q545 347 538 360 L505 403
         L538 446 Q545 459 560 459 H580 A22 22 0 0 0 620 459 A22 22 0 0 1 660 459 A22 22 0 0 0 700 459 A22 22 0 0 1 740 459 H760
         Q772 459 772 471 V519 Q772 531 760 531 H540 Q530 531 525 524 Z"/>

    <!-- back panel copy (upside down) -->
    <g class="back-claim serif bold" transform="rotate(180 668 230)" fill="var(--cream)" text-anchor="middle">
      <text x="668" y="205" font-size="14">ABRASIVES &amp; ACCESSORIES</text>
      <text x="668" y="222" font-size="12">Cut, Quality Checked &amp;</text>
      <text x="668" y="240" font-size="12">Packed in New Zealand</text>
      <text x="668" y="258" font-size="12">from imported materials</text>
    </g>

    <g class="back-address serif bold" transform="rotate(180 357 343)" fill="var(--cream)" text-anchor="middle" font-size="16">
      <text x="357" y="305">New Zealand</text>
      <text x="357" y="334">West Auckland</text>
      <text x="357" y="361">456 Lane</text>
      <text x="357" y="391">QRV Abrasives</text>
    </g>

    <!-- brand name -->
    <g class="brand-name serif bold" fill="var(--steel)" text-anchor="middle" font-size="30">
      <text x="357" y="500">LUMEN</text>
      <text x="357" y="540">RIDGE</text>
    </g>

    <!-- range line -->
    <text class="range-line serif bold" x="622" y="570" text-anchor="middle" font-size="15" fill="var(--cream)">ABRASIVES &amp; ACCESSORIES</text>

    <!-- guarantee seal -->
    <g class="guarantee-seal">
      <circle cx="320" cy="713" r="48" fill="var(--card-black)" stroke="var(--cream)" stroke-width="3"/>
      <text class="serif bold" x="320" y="708" text-anchor="middle" font-size="14" fill="var(--paper)">Quality</text>
      <text class="serif bold" x="320" y="727" text-anchor="middle" font-size="14" fill="var(--paper)">Garantee</text>
    </g>

    <!-- product over-sticker info -->
    <g class="product-info serif bold" fill="var(--ink)">
      <g transform="rotate(180 1040 140)" font-size="13">
        <text x="1040" y="180" text-anchor="middle">Product 123456</text>
        <text x="1040" y="112" text-anchor="middle">125mm X 8 Hole P80</text>
      </g>

      <rect x="917" y="430" width="148" height="47" rx="5" fill="none" stroke="var(--ink)" stroke-width="2"/>
      <text x="991" y="462" text-anchor="middle" font-size="22">P 80</text>

      <text x="995" y="563" text-anchor="middle" font-size="29" fill="var(--plum)">SANDING</text>
      <text x="995" y="606" text-anchor="middle" font-size="29" fill="var(--plum)">DISCS</text>

      <text x="995" y="690" text-anchor="middle" font-size="18" fill="var(--plum)">125mm X 8 Hole</text>

      <rect x="952" y="722" width="88" height="44" rx="4" fill="none" stroke="var(--ink)" stroke-width="2"/>
      <text x="996" y="751" text-anchor="middle" font-size="17">QTY 5</text>
    </g>

    <!-- colour palette -->
    <g class="palette" stroke="#555" stroke-width="1">
      <rect x="428" y="1110" width="60" height="60" fill="var(--paper)"/>
      <rect x="504" y="1110" width="60" height="60" fill="var(--cream)" stroke="none"/>
      <rect x="580" y="1110" width="60" height="60" fill="var(--steel)" stroke="none"/>
      <rect x="656" y="1110" width="60" height="60" fill="var(--grey)" stroke="none"/>
      <rect x="732" y="1110" width="60" height="60" fill="var(--plum)" stroke="none"/>
      <rect x="808" y="1110" width="60" height="60" fill="var(--ink)" stroke="none"/>
    </g>
  </svg>
</div>
</body>
</html>
```